Business Card Design

We are a manufacturing and distribution company with most of our customer base being supermarkets. We have established brand guidelines that are attached.

```html
<!DOCTYPE html>
<html lang="en">
<head>
<meta charset="utf-8">
<title>Corvane Business Card</title>
<link href="https://fonts.googleapis.com/css2?family=Roboto:wght@300;400;700&display=swap" rel="stylesheet">
<style>
  :root{
    --bg:#d2d5d6;
    --paper:#f1f1ef;
    --ink:#1a1a1a;
    --night:#232425;
    --brand-blue:#0d3b8f;
    --edge-blue:#1e6fc0;
    --brand-red:#d3111a;
    --grey-text:#4a4a4a;
    --silver:#e6e6e6;
  }
  html,body{margin:0;padding:0;width:1200px;height:1049px;overflow:hidden;background:var(--bg);}
  body{font-family:'Roboto',Arial,sans-serif;position:relative;}

  .card{position:absolute;box-shadow:0 18px 40px rgba(0,0,0,.22);box-sizing:border-box;}

  /* front */
  .card-front{left:70px;top:215px;width:350px;height:612px;background:var(--paper);border-bottom:4px solid var(--edge-blue);padding:64px 38px 0 52px;}
  .brand{display:flex;align-items:center;gap:14px;}
  .brand-square{width:34px;height:34px;background:var(--brand-red);flex:none;}
  .brand-name{font-weight:700;font-size:46px;letter-spacing:1px;color:var(--ink);line-height:1;}
  .person{margin-top:92px;}
  .person-name{font-weight:400;font-size:21px;letter-spacing:.5px;color:var(--brand-blue);text-transform:uppercase;line-height:1.15;}
  .person-title{font-weight:300;font-size:21px;color:var(--brand-red);line-height:1.15;}
  .address{margin-top:58px;font-weight:300;font-size:17px;color:var(--grey-text);line-height:1.5;}
  .contacts{margin-top:22px;list-style:none;padding:0;font-weight:300;font-size:17px;color:var(--grey-text);line-height:1.5;}
  .contacts li{display:flex;align-items:center;gap:10px;}
  .contacts svg{width:15px;height:15px;flex:none;fill:none;stroke:var(--brand-red);stroke-width:2;}

  /* back */
  .card-back{left:520px;top:352px;width:612px;height:350px;background:var(--night);border-bottom:6px solid var(--edge-blue);display:flex;align-items:center;justify-content:center;}
  .card-back .brand-name{color:var(--silver);font-size:62px;letter-spacing:2px;}
  .card-back .brand-square{width:44px;height:44px;}
</style>
</head>
<body>
  <section class="card card-front">
    <div class="brand">
      <span class="brand-square"></span>
      <span class="brand-name">CORVANE</span>
    </div>
    <div class="person">
      <div class="person-name">Lukas M. Brenner</div>
      <div class="person-title">Managing Director</div>
    </div>
    <div class="address">
      Corvane DP<br>
      482 Rue Laurier Montreal<br>
      Quebec H2T 3K9
    </div>
    <ul class="contacts">
      <li><svg viewBox="0 0 16 16"><path d="M4 2l2 3-1.5 1.5a8 8 0 0 0 5 5L11 10l3 2-1 2.5C7 14 2 9 1.5 3z"/></svg>(555) 310-4200</li>
      <li><svg viewBox="0 0 16 16"><rect x="4.5" y="1.5" width="7" height="13" rx="1"/><line x1="7" y1="12" x2="9" y2="12"/></svg>(555) 310-4817</li>
      <li><svg viewBox="0 0 16 16"><rect x="1.5" y="3.5" width="13" height="9"/><path d="M1.5 3.5l6.5 5 6.5-5"/></svg>info@corvane-example.com</li>
      <li><svg viewBox="0 0 16 16"><circle cx="8" cy="8" r="6.5"/><ellipse cx="8" cy="8" rx="3" ry="6.5"/><line x1="1.5" y1="8" x2="14.5" y2="8"/></svg>www.corvane-example.com</li>
    </ul>
  </section>

  <section class="card card-back">
    <div class="brand">
      <span class="brand-square"></span>
      <span class="brand-name">CORVANE</span>
    </div>
  </section>
</body>
</html>
```